Disease outbreak warning

I need a flyer that explains to hunters how to act as frontline responders to potential disease outbreaks in wildlife populations. In this case the disease is African Swine Fever. We need an at a glance style with plenty of colour and that’s very easy to read.

I HAVE ATTACHED SOME EXISTING FLYERS FROM OVERSEAS ETC THAT CONTAIN SOME OF THE RELEVANT INFO. THEY ARE TO BE USED AS A GUIDE ONLY.
Updates

Need to see some more options. We have some that can be developed successfully but we’d like to see some more options that will suit a national campaign.

Target Market(s)

Australian hunters encountering wild pigs. Typical age is from 18 to 32 but can be older. Male or female.

Colors

Designer to choose colors to be used in the design.

Requirements
Must have
• The KVRTE logo (supplied). It should be relatively small at the bottom of the page. Plus we need room for two or three other logos that can be overprinted on the project if required.
• Must have information for hunters as the main focus.
Nice to have
• A double sided flyer.
Should not have
• US spelling.

```html
<!DOCTYPE html>
<html lang="en">
<head>
<meta charset="utf-8">
<title>African Swine Fever – Double Sided Flyer</title>
<link rel="stylesheet" href="https://fonts.googleapis.com/css2?family=Rubik:wght@700;800;900&family=Montserrat:wght@400;600;700&display=swap">
<style>
  :root {
    --navy: #0d2a8e;
    --orange: #f39a1e;
    --white: #ffffff;
    --paper: #efefef;
    --map-beige: #ecebc4;
    --map-ink: #3a3a33;
    --forest: #4fa63a;
    --olive: #7d7a4c;
    --boar: #c46a58;
    --pin-teal: #1f8f9a;
    --pin-red: #e2422c;
    --trail-red: #e2422c;
  }
  html, body {
    margin: 0;
    padding: 0;
    width: 1200px;
    height: 2400px;
    overflow: hidden;
    background: var(--paper);
  }
  .canvas {
    position: relative;
    width: 1200px;
    height: 2400px;
  }
  .flyer {
    position: absolute;
    left: 214px;
    width: 772px;
    height: 1178px;
    display: block;
  }
  .flyer--front { top: 12px; }
  .flyer--back { top: 1210px; }

  .display { font-family: "Rubik", "Arial Rounded MT Bold", sans-serif; font-weight: 900; }
  .display-light { font-family: "Rubik", sans-serif; font-weight: 700; }
  .body { font-family: "Montserrat", Arial, sans-serif; font-weight: 400; }
  .body-bold { font-family: "Montserrat", Arial, sans-serif; font-weight: 700; }

  .fill-orange { fill: var(--orange); }
  .fill-white { fill: var(--white); }
  .fill-navy { fill: var(--navy); }
  .fill-ink { fill: var(--map-ink); }
</style>
</head>
<body>
<main class="canvas">

  <!-- Side one -->
  <svg class="flyer flyer--front" viewBox="0 0 601 917" xmlns="http://www.w3.org/2000/svg">
    <defs>
      <linearGradient id="hunterTones" x1="0" y1="0" x2="0" y2="1">
        <stop offset="0" stop-color="#c9b98a"/>
        <stop offset="0.5" stop-color="#8c8a52"/>
        <stop offset="1" stop-color="#6e4a2c"/>
      </linearGradient>
      <linearGradient id="boarTones" x1="0" y1="0" x2="1" y2="1">
        <stop offset="0" stop-color="#d27b66"/>
        <stop offset="1" stop-color="#a9554a"/>
      </linearGradient>
      <linearGradient id="treeTones" x1="0" y1="0" x2="0" y2="1">
        <stop offset="0" stop-color="#5fb443"/>
        <stop offset="1" stop-color="#3f8b2f"/>
      </linearGradient>
    </defs>

    <rect class="fill-navy" width="601" height="917"/>

    <g class="headline">
      <text class="display fill-orange" x="300" y="92" font-size="37" text-anchor="middle">AFRICAN SWINE FEVER</text>
      <text class="display fill-white" x="300" y="127" text-anchor="middle"><tspan font-size="29">Hunters</tspan><tspan font-size="20"> can make </tspan><tspan font-size="29">the difference</tspan></text>
    </g>

    <circle class="focus-ring" cx="140" cy="345" r="165" fill="none" stroke="#ffffff" stroke-width="1.2"/>

    <g class="hunter-illustration" role="img" aria-label="Illustration of a bearded hunter with rifle and backpack in front of a pine tree">
      <path d="M0 235 Q150 210 300 250 L300 555 L0 555 Z" fill="url(#hunterTones)" opacity="0.9"/>
    </g>

    <g class="trail-dots">
      <circle cx="292" cy="400" r="4" class="fill-white"/>
      <circle cx="288" cy="420" r="4" class="fill-orange"/>
      <circle cx="284" cy="440" r="4" class="fill-white"/>
      <circle cx="278" cy="460" r="4" class="fill-orange"/>
      <circle cx="270" cy="480" r="4" class="fill-white"/>
    </g>

    <g class="connectors" stroke="#f39a1e" stroke-width="1.2" fill="none">
      <polyline points="268,213 298,188 350,188"/>
      <polyline points="340,393 390,345 420,345"/>
      <polyline points="140,538 190,590"/>
    </g>
    <g class="connector-dots">
      <circle cx="268" cy="213" r="7" class="fill-orange"/>
      <circle cx="340" cy="393" r="7" class="fill-orange"/>
      <circle cx="140" cy="538" r="7" class="fill-orange"/>
    </g>

    <text class="body-bold fill-white" font-size="13.8" text-anchor="end">
      <tspan x="555" y="178">African swine fever (ASF)</tspan>
      <tspan x="555" y="195">is a devastating, usually</tspan>
      <tspan x="555" y="212">deadly, infectious disease</tspan>
      <tspan x="555" y="229">of pigs and wild boar for</tspan>
      <tspan x="555" y="246">which no vaccine exists</tspan>
    </text>

    <g class="icon-syringe" fill="none" stroke="#ffffff" stroke-width="2.4" stroke-linejoin="round">
      <line x1="404" y1="290" x2="446" y2="290"/>
      <rect x="446" y="277" width="66" height="26" rx="4"/>
      <line x1="512" y1="290" x2="526" y2="290"/>
      <line x1="526" y1="276" x2="526" y2="304"/>
      <line x1="534" y1="274" x2="534" y2="306"/>
      <line x1="458" y1="277" x2="458" y2="303"/>
      <line x1="478" y1="296" x2="478" y2="290"/>
      <line x1="485" y1="296" x2="485" y2="286"/>
      <line x1="492" y1="296" x2="492" y2="290"/>
      <line x1="499" y1="296" x2="499" y2="284"/>
    </g>

    <text class="display fill-orange" font-size="20" text-anchor="end">
      <tspan x="555" y="340">Transmission</tspan>
      <tspan x="555" y="364">and Spread</tspan>
    </text>
    <text class="body fill-white" font-size="14.6" text-anchor="end">
      <tspan x="555" y="385">Transmission can</tspan>
      <tspan x="555" y="401.5">happen through direct</tspan>
      <tspan x="555" y="418">contact of healthy pigs</tspan>
      <tspan x="555" y="434.5">or wild boar with infect-</tspan>
      <tspan x="555" y="451">ed (dead or sick) pigs or</tspan>
      <tspan x="555" y="467.5">wild boar. However,</tspan>
      <tspan x="555" y="484">humans and especially</tspan>
      <tspan x="555" y="500.5">hunters - while not being</tspan>
      <tspan x="555" y="517">affected by the disease.</tspan>
    </text>

    <g class="boar-illustration" role="img" aria-label="Illustration of a wild boar">
      <path d="M272 600 Q330 520 470 525 Q545 535 540 600 L530 655 L300 655 Z" fill="url(#boarTones)"/>
    </g>

    <text class="display fill-orange" font-size="19">
      <tspan x="72" y="600">Can help</tspan>
      <tspan x="72" y="624">spreading it by:</tspan>
    </text>

    <text class="body fill-white" font-size="13.2">
      <tspan x="78" y="684"><tspan class="body-bold">• Any contact with infected animals and dead bodies</tspan> (carcasses).</tspan>
      <tspan x="78" y="708"><tspan class="body-bold">• Contact with anything contaminated by the virus</tspan> (e.g. clothing,</tspan>
      <tspan x="78" y="724">vehicles, other equipment).</tspan>
      <tspan x="78" y="749" class="body-bold">• Feeding the animals with meat or meat products from</tspan>
      <tspan x="78" y="765"><tspan class="body-bold">infected animals</tspan> (e.g. sausages or uncooked meat) or</tspan>
      <tspan x="78" y="781">garbage containing infected meat (e.g. kitchen</tspan>
      <tspan x="78" y="797">waste, swill feed, including offal).</tspan>
    </text>

    <path class="footer-band" d="M0 818 C200 880 420 830 601 715 L601 917 L0 917 Z" fill="var(--orange)"/>
    <path class="footer-base" d="M0 852 C200 905 430 862 601 758 L601 917 L0 917 Z" fill="var(--white)"/>

    <g class="tree-illustration" role="img" aria-label="Illustration of a green tree">
      <path d="M0 650 Q45 700 55 800 L40 917 L0 917 Z" fill="url(#treeTones)"/>
    </g>

    <g class="client-mark">
      <circle cx="493" cy="866" r="9" fill="var(--navy)"/>
      <text class="display fill-navy" x="508" y="873" font-size="19">KVRTE</text>
    </g>
  </svg>

  <!-- Side two -->
  <svg class="flyer flyer--back" viewBox="0 0 601 917" xmlns="http://www.w3.org/2000/svg">
    <defs>
      <linearGradient id="treeTonesBack" x1="0" y1="0" x2="0" y2="1">
        <stop offset="0" stop-color="#78bf3f"/>
        <stop offset="1" stop-color="#4c9a2c"/>
      </linearGradient>
      <linearGradient id="hunterTonesBack" x1="0" y1="0" x2="1" y2="1">
        <stop offset="0" stop-color="#6f6b4a"/>
        <stop offset="1" stop-color="#4f4b35"/>
      </linearGradient>
    </defs>

    <rect class="fill-orange" width="601" height="917"/>

    <g class="treetop-illustration" role="img" aria-label="Illustration of leafy trees">
      <path d="M390 140 Q400 40 480 35 Q575 35 585 130 L585 145 L390 145 Z" fill="url(#treeTonesBack)"/>
    </g>

    <g class="headline">
      <text class="display fill-navy">
        <tspan x="48" y="92" font-size="28">Hunters</tspan><tspan font-size="18"> have a</tspan>
      </text>
      <text class="display fill-navy" x="48" y="122" font-size="28">key role to play</text>
      <text class="body-bold fill-white" font-size="14.2">
        <tspan x="48" y="155">During your hunting trips, especially to</tspan>
        <tspan x="48" y="172">the areas considered at risk, you should:</tspan>
      </text>
    </g>

    <g class="map-illustration" role="img" aria-label="Illustration of a folded hunting-ground map with river, trails and trees">
      <polygon points="48,258 580,128 601,128 601,592 168,662" fill="var(--navy)"/>
      <polygon points="76,272 601,160 601,578 182,644" fill="var(--map-beige)"/>
    </g>

    <g class="hunter-illustration" role="img" aria-label="Illustration of a hunter in a cap holding a rifle, seen from the side">
      <path d="M0 540 L70 540 Q150 560 180 640 L330 640 L330 680 L200 700 L180 917 L0 917 Z" fill="url(#hunterTonesBack)"/>
    </g>

    <g class="tree-illustration" role="img" aria-label="Illustration of leafy and pine trees">
      <path d="M250 680 Q330 620 450 625 Q590 630 601 700 L601 917 L470 917 L470 725 Q380 705 250 705 Z" fill="url(#treeTonesBack)"/>
    </g>

    <g class="map-notes fill-ink body" font-size="11.6">
      <text transform="rotate(-9 335 300)" text-anchor="end">
        <tspan x="335" y="262">&gt; Contribute to the gradual</tspan>
        <tspan x="335" y="276">reduction of the wild boar</tspan>
        <tspan x="335" y="290">density in the areas not yet</tspan>
        <tspan x="335" y="304">affected by the disease,</tspan>
        <tspan x="335" y="318">including targeted</tspan>
        <tspan x="335" y="332">hunting of adult</tspan>
        <tspan x="335" y="346">and sub-adult</tspan>
        <tspan x="335" y="360">females.</tspan>
      </text>
      <text transform="rotate(-9 135 410)">
        <tspan x="135" y="400">&gt; Collaborate</tspan>
        <tspan x="135" y="414">with the competent</tspan>
        <tspan x="135" y="428">authority in the finding</tspan>
        <tspan x="135" y="442">and reporting of</tspan>
        <tspan x="135" y="456">wild boar carcasses.</tspan>
      </text>
      <text transform="rotate(-22 455 270)">
        <tspan x="455" y="238">Clean and</tspan>
        <tspan x="455" y="252">disinfect your</tspan>
        <tspan x="455" y="266">equipment,</tspan>
        <tspan x="455" y="280">clothes, vehicle</tspan>
        <tspan x="455" y="294">and trophies on</tspan>
        <tspan x="455" y="308">site and always</tspan>
        <tspan x="455" y="322">before leaving</tspan>
        <tspan x="455" y="336">the area.</tspan>
      </text>
      <text transform="rotate(-6 360 440)">
        <tspan x="360" y="428">&gt; Eviscerate shot wild</tspan>
        <tspan x="360" y="442">boar in the designated</tspan>
        <tspan x="360" y="456">dressing area of the</tspan>
        <tspan x="360" y="470">hunting ground.</tspan>
      </text>
      <text transform="rotate(-9 285 575)">
        <tspan x="285" y="568">&gt; Do not feed wild boar</tspan>
        <tspan x="285" y="582">throughout the whole year.</tspan>
      </text>
    </g>

    <g class="icon-pin icon-pin--teal">
      <path d="M555 392 a14 14 0 0 1 14 14 c0 12 -14 26 -14 26 c0 0 -14 -14 -14 -26 a14 14 0 0 1 14 -14 Z" fill="var(--pin-teal)"/>
      <circle cx="555" cy="406" r="6" fill="none" stroke="var(--map-beige)" stroke-width="2.4"/>
    </g>
    <g class="icon-pin icon-pin--red">
      <path d="M205 535 a14 14 0 0 1 14 14 c0 12 -14 26 -14 26 c0 0 -14 -14 -14 -26 a14 14 0 0 1 14 -14 Z" fill="var(--pin-red)"/>
      <circle cx="205" cy="549" r="6" fill="none" stroke="var(--map-beige)" stroke-width="2.4"/>
    </g>

    <text class="display-light fill-white" font-size="14.4" text-anchor="middle">
      <tspan x="372" y="760">If you see unusual wild</tspan>
      <tspan x="372" y="777.5">boar behaviour or, most</tspan>
      <tspan x="372" y="795">likely, if you find a dead</tspan>
      <tspan x="372" y="812.5">animal, you should con-</tspan>
      <tspan x="372" y="830">sider the possibility that</tspan>
      <tspan x="372" y="847.5">it has been infected by</tspan>
      <tspan x="372" y="865" class="fill-navy">African Swine Fever</tspan>
    </text>
  </svg>

</main>
</body>
</html>
```